Bags for ethnic grocery store

Need to create poly and paper bag design for the "Ethnic grocery store". Need show case a modern design with the shop logo / tag line as well as home delivery options ( phone, whatsapp, ecomerce, walk in )
Tag line: One stop shop for Pakistani products

Target Market(s)

House holds who are doing grocery shopping

Industry/Entity Type

Grocery Store

Colors

Designer to choose colors to be used in the design.

Requirements
Must have
• Green and white color usage, modern design

```html
<!DOCTYPE html>
<html lang="en">
<head>
<meta charset="utf-8">
<title>The Crescent Bazaar – Bag Designs</title>
<link href="https://fonts.googleapis.com/css2?family=Josefin+Sans:wght@400;600;700&family=Special+Elite&display=swap" rel="stylesheet">
<style>
  :root {
    --backdrop: #ecebe8;
    --kraft: #c9a57b;
    --kraft-fold: #b8936a;
    --poly: #fbfbfb;
    --poly-edge: #dcdcdc;
    --brand-green: #1f7a3a;
    --ink: #2b2b2b;
    --ink-soft: #4a4a4a;
    --art-teal: #2a9a9a;
    --art-red: #d8412f;
    --art-yellow: #f1c232;
    --art-green: #1d6b34;
    --art-pink: #e0567e;
    --art-blue: #2f5fa8;
    --panel-cream: #f6eddc;
    --tagline-ink: #1f2f2a;
  }
  * { box-sizing: border-box; margin: 0; padding: 0; }
  html, body { width: 686px; height: 1200px; overflow: hidden; }
  body {
    background: var(--backdrop);
    font-family: "Josefin Sans", sans-serif;
    color: var(--ink);
    position: relative;
  }

  .bag { position: absolute; }

  /* Paper bags */
  .paper-bag {
    top: 60px; width: 260px; height: 420px;
    background: var(--kraft);
    border-radius: 3px;
  }
  .paper-bag::before {
    content: ""; position: absolute; left: 0; right: 0; top: 0; height: 26px;
    background: var(--kraft-fold);
  }
  .paper-bag--front { left: 60px; }
  .paper-bag--back { left: 366px; }

  /* Poly bags */
  .poly-bag { top: 610px; width: 290px; height: 560px; }
  .poly-bag--front { left: 40px; }
  .poly-bag--back { left: 356px; }
  .poly-bag svg.bag-shape { position: absolute; inset: 0; }

  /* Brand block */
  .brand { position: absolute; left: 0; right: 0; text-align: center; }
  .brand-illustration {
    margin: 0 auto; border-radius: 4px;
    background: linear-gradient(180deg, rgba(90,90,90,.12), rgba(90,90,90,.32));
  }
  .brand-name {
    font-family: "Josefin Sans", sans-serif;
    font-weight: 700; color: var(--brand-green);
    line-height: 1.05; margin-top: 10px; white-space: nowrap;
  }
  .brand-name .line { display: block; }
  .brand-name .mark {
    display: inline-block; border-radius: 50%;
    background: var(--brand-green); vertical-align: middle; margin-right: 6px;
    position: relative; top: -3px;
  }

  .contact { position: absolute; left: 0; right: 0; text-align: center; color: var(--ink); }
  .contact-line { font-weight: 600; letter-spacing: .04em; text-transform: uppercase; white-space: nowrap; }
  .contact-line .chat-dot {
    display: inline-block; border-radius: 50%;
    background: var(--ink-soft); vertical-align: middle; margin-right: 5px;
    position: relative; top: -1px;
  }

  .paper-bag .brand { top: 48px; }
  .paper-bag .brand-illustration { width: 150px; height: 80px; }
  .paper-bag .brand-name { font-size: 27px; }
  .paper-bag .brand-name .mark { width: 12px; height: 12px; }
  .paper-bag .contact { top: 262px; }
  .paper-bag .contact-line { font-size: 9.5px; margin-bottom: 8px; }
  .paper-bag .chat-dot { width: 10px; height: 10px; }

  .poly-bag .brand { top: 190px; }
  .poly-bag .brand-illustration { width: 170px; height: 96px; }
  .poly-bag .brand-name { font-size: 30px; }
  .poly-bag .brand-name .mark { width: 13px; height: 13px; }
  .poly-bag .contact { top: 416px; }
  .poly-bag .contact-line { font-size: 10px; margin-bottom: 9px; }
  .poly-bag .chat-dot { width: 10px; height: 10px; }

  /* Truck-art panel with plain layered frame */
  .art-panel {
    position: absolute;
    border: 5px solid var(--art-green);
    outline: 4px solid var(--art-red);
    outline-offset: 0;
    box-shadow: inset 0 0 0 4px var(--art-yellow), inset 0 0 0 8px var(--art-teal);
  }
  .art-fill {
    position: absolute; inset: 8px;
    background:
      radial-gradient(circle at 50% 24%, rgba(29,107,52,.55), transparent 38%),
      radial-gradient(circle at 12% 10%, rgba(224,86,126,.55), transparent 35%),
      radial-gradient(circle at 88% 10%, rgba(47,95,168,.45), transparent 35%),
      radial-gradient(circle at 15% 90%, rgba(241,194,50,.7), transparent 40%),
      radial-gradient(circle at 85% 90%, rgba(42,154,154,.6), transparent 40%),
      linear-gradient(180deg, #e8d9a8, #e6b86a 55%, #d97a52);
  }
  .tagline-box {
    position: absolute; left: 8%; right: 8%;
    background: var(--panel-cream);
    border-top: 3px solid var(--art-red);
    border-bottom: 3px solid var(--art-red);
    padding: 10px 6px; text-align: center;
    font-family: "Special Elite", monospace;
    color: var(--tagline-ink); line-height: 1.35;
  }
  .paper-bag .art-panel { left: 30px; top: 52px; width: 200px; height: 316px; }
  .paper-bag .tagline-box { top: 148px; font-size: 15px; }
  .poly-bag .art-panel { left: 30px; top: 172px; width: 230px; height: 360px; }
  .poly-bag .tagline-box { top: 168px; font-size: 17px; }
</style>
</head>
<body>

  <section class="bag paper-bag paper-bag--front">
    <div class="brand">
      <div class="brand-illustration" role="img" aria-label="Line drawing of a historic market hall with a clock tower"></div>
      <p class="brand-name"><span class="line"><span class="mark"></span>The Crescent</span><span class="line">Bazaar</span></p>
    </div>
    <div class="contact">
      <p class="contact-line">14 Lahore Rd. Leeds</p>
      <p class="contact-line">(99) 4410 2286</p>
      <p class="contact-line">www.thecrescentbazaar.uk</p>
      <p class="contact-line"><span class="chat-dot"></span>thecrescentbazaar_online</p>
    </div>
  </section>

  <section class="bag paper-bag paper-bag--back">
    <div class="art-panel">
      <div class="art-fill" role="img" aria-label="Colourful Pakistani truck-art pattern with a green floral medallion and corner flourishes"></div>
      <p class="tagline-box">One stop shop for Pakistani products</p>
    </div>
  </section>

  <section class="bag poly-bag poly-bag--front">
    <svg class="bag-shape" width="290" height="560" viewBox="0 0 290 560" aria-hidden="true">
      <path d="M0 560 V20 Q0 0 20 0 H60 Q75 0 78 20 Q90 110 145 115 Q200 110 212 20 Q215 0 230 0 H270 Q290 0 290 20 V560 Z" fill="var(--poly)" stroke="var(--poly-edge)"/>
    </svg>
    <div class="brand">
      <div class="brand-illustration" role="img" aria-label="Line drawing of a historic market hall with a clock tower"></div>
      <p class="brand-name"><span class="line"><span class="mark"></span>The Crescent</span><span class="line">Bazaar</span></p>
    </div>
    <div class="contact">
      <p class="contact-line">14 Lahore Rd. Leeds</p>
      <p class="contact-line">(99) 4410 2286</p>
      <p class="contact-line">www.thecrescentbazaar.uk</p>
      <p class="contact-line"><span class="chat-dot"></span>thecrescentbazaar_online</p>
    </div>
  </section>

  <section class="bag poly-bag poly-bag--back">
    <svg class="bag-shape" width="290" height="560" viewBox="0 0 290 560" aria-hidden="true">
      <path d="M0 560 V20 Q0 0 20 0 H60 Q75 0 78 20 Q90 110 145 115 Q200 110 212 20 Q215 0 230 0 H270 Q290 0 290 20 V560 Z" fill="var(--poly)" stroke="var(--poly-edge)"/>
    </svg>
    <div class="art-panel">
      <div class="art-fill" role="img" aria-label="Colourful Pakistani truck-art pattern with a green floral medallion and corner flourishes"></div>
      <p class="tagline-box">One stop shop for Pakistani products</p>
    </div>
  </section>

</body>
</html>
```